Update Wordpress website to be captivating, modern and concise

Help us create a cohesive brand and deliver our marketing messages more concisely. We would like to update our Wordpress website to be clean, modern and captivating. Please see the uploaded file for more information on our company, our current website and how we want to continue the relationship beyond the contest. Thank you and we look forward to receiving your creative ideas!

Update: We no longer need you to complete the development.
Updates

We no longer require you to implement the design in Wordpress. Please provide your best, creative designs. Thanks

Target Market(s)

Our customers are companies who are looking for sleek, sexy, easy to use mobile applications for their sales teams. Our customers range from your small to Zenlow 300.

Industry/Entity Type

Marketing

Font styles to use
Sans Serif

Requirements
Must have
• Clean, contemporary, engaging. Comes across as easy to use and inviting. Use the blue in our logo. We do a lot of work on Quorvel Apps and therefore our standard is the Quorvel UX for our styling and UI.
Should not have
• Clutter and distracting.

```html
<!DOCTYPE html>
<html lang="en">
<head>
<meta charset="utf-8">
<title>Brightwell Analytics</title>
<link rel="stylesheet" href="https://fonts.googleapis.com/css2?family=Open+Sans:wght@300;400;600;700&display=swap">
<style>
:root{
  --blue:#1a9fd0;
  --blue-deep:#0b8fbf;
  --sky:#6cc4f2;
  --circle:#7ccdf7;
  --ink:#2a3843;
  --text:#555e66;
  --muted:#888;
  --white:#fff;
  --pale:#dff2f7;
  --ring:#e3e3e3;
}
*{box-sizing:border-box;margin:0;padding:0}
html,body{width:1200px;height:2927px;overflow:hidden}
body{font-family:"Open Sans",Arial,sans-serif;background:var(--white);color:var(--text);position:relative}
.abs{position:absolute}

/* hero */
.hero{left:0;top:0;width:1200px;height:468px;background:linear-gradient(135deg,#1aa7d8 0%,#0f8fc2 45%,#1ba3d2 70%,#0c86b6 100%)}
.brand{left:117px;top:30px;display:flex;align-items:center;gap:12px;color:var(--white);font-weight:600;font-size:19px;line-height:1.05}
.brand-dot{width:40px;height:40px;border:2px solid var(--white);border-radius:50%}
.nav{left:0;top:42px;width:1200px}
.nav a{position:absolute;color:var(--white);text-decoration:none;font-size:13px}
.nav .current{border-bottom:2px solid var(--white);padding-bottom:6px}
.hero-title{left:211px;top:160px;color:var(--white);font-weight:300;font-size:44px;line-height:46px}
.btn-ghost{display:inline-flex;align-items:center;gap:8px;border:2px solid var(--white);border-radius:4px;color:var(--white);font-size:24px;font-weight:300}
.hero-btn{left:217px;top:277px;width:187px;height:41px;justify-content:center}
.video{left:620px;top:123px;width:461px;height:263px;border:3px solid #d8f1fb;border-radius:4px;background:#7fcbf2;overflow:hidden}
.video-art{position:absolute;left:0;top:0;width:455px;height:230px;background:linear-gradient(120deg,#8ad2f6,#6cc1ee)}
.video-bar{position:absolute;left:0;bottom:0;width:455px;height:27px;background:#1b2630}

/* award strip */
.strip{left:0;top:468px;width:1200px;height:69px;background:var(--ink);color:var(--white);font-size:20px}
.strip span{position:absolute;top:21px}
.badge{left:386px;top:459px;width:87px;height:87px;border-radius:50%;background:var(--white);border:4px solid var(--ink);display:flex;align-items:center;justify-content:center;font-style:italic;font-size:34px;color:var(--ink)}

/* about */
.about-art{left:146px;top:634px;width:440px;height:410px;border-radius:50% 50% 12px 12px;background:radial-gradient(circle at 50% 55%,#f2fbff 0%,#e2f5fd 60%,#fff 100%)}
.about{left:671px;top:737px;width:380px}
.about h2{font-size:18px;font-weight:600;color:#333;margin-bottom:10px}
.about p{font-size:12.5px;line-height:18px;color:var(--muted)}
.btn-small{display:inline-flex;align-items:center;gap:6px;border:1.5px solid var(--blue);border-radius:3px;color:var(--blue);font-size:14px;padding:2px 10px;margin-top:22px}

/* challenge banner */
.banner{left:0;top:1122px;width:1200px;height:150px;background:var(--ink)}
.banner-ribbon{left:446px;top:1178px;width:484px;height:44px;border:2px solid var(--white);color:var(--white);font-size:19px;display:flex;align-items:center;justify-content:center;transform:rotate(3deg)}

/* services */
.service{top:1362px;width:240px;text-align:center}
.service-disc{width:178px;height:178px;margin:0 auto;border-radius:50%;background:var(--circle);border:8px solid var(--ring);display:flex;align-items:center;justify-content:center}
.service h3{font-weight:400;font-size:17px;color:#444;margin-top:22px}
.service .btn-small{margin-top:14px;font-size:16px;padding:3px 12px}

/* forum band */
.forum{left:0;top:1717px;width:1200px;height:68px;background:var(--blue-deep);color:var(--white);font-size:20px;text-align:center;line-height:68px;z-index:2}
.partners-cap{left:484px;top:1785px;width:218px;height:104px;border-radius:0 0 109px 109px / 0 0 104px 104px;border:2px solid var(--blue);border-top:none;background:var(--white)}
.partners-cap h2{position:absolute;top:20px;width:100%;text-align:center;font-size:19px;font-weight:700;color:#222}
.partners-cap svg{position:absolute;left:103px;top:62px}
.arrow-btn{top:1967px;width:44px;height:44px;border:2px solid #aaa;border-radius:50%}
.partner{top:1962px;font-size:44px;color:#555;font-weight:400}

/* blog */
.blog{left:0;top:2133px;width:1200px;height:739px;background:linear-gradient(135deg,#d4f0f6 0%,#e8f8fb 40%,#d9f2f6 70%,#dcecea 100%)}
.blog-title{left:0;top:2214px;width:1200px;text-align:center;font-size:19px;font-weight:700;color:#222}
.timeline{left:610px;top:2262px;height:610px;border-left:2px dashed #9fc8d2}
.post-photo{width:176px;height:176px;border-radius:50%;border:2px dashed #8fbcc8;padding:8px}
.post-photo div{width:100%;height:100%;border-radius:50%;background:linear-gradient(160deg,#f5e9e2,#d7c2b4 55%,#a3b8cc)}
.post h3{font-size:19px;font-weight:600;color:#222;margin-bottom:12px;white-space:nowrap}
.post p{font-size:12.5px;line-height:19px;color:#888}
.post time{display:block;font-size:8.5px;font-weight:600;color:#333;margin-top:6px;letter-spacing:.3px}
.post .more{display:inline-flex;align-items:center;gap:8px;font-size:16px;color:#222;margin-top:12px}

/* footer */
.footer{left:0;top:2872px;width:1200px;height:55px;background:var(--blue-deep);color:var(--white);font-size:9px}
.social{top:14px;width:26px;height:26px;border-radius:50%;background:var(--white)}
</style>
</head>
<body>

<section class="abs hero"></section>
<div class="abs brand"><span class="brand-dot"></span><span>Brightwell<br>Analytics</span></div>
<nav class="abs nav">
  <a class="current" style="left:753px">Home</a>
  <a style="left:835px">Blog</a>
  <a style="left:907px">About Us</a>
  <a style="left:1001px">Join the Team</a>
</nav>
<h1 class="abs hero-title">Drive Actions<br>&amp; Results</h1>
<div class="abs btn-ghost hero-btn">Get Started
  <svg width="16" height="18" viewBox="0 0 16 18"><path d="M2 2 L14 9 L2 16 Z" fill="none" stroke="#fff" stroke-width="2"/></svg>
</div>
<div class="abs video">
  <div class="video-art" role="img" aria-label="Video still: animated presenter beside the words Relevant, Timely Answers"></div>
  <div class="video-bar">
    <svg width="455" height="27" viewBox="0 0 455 27">
      <path d="M10 8 L19 13.5 L10 19 Z" fill="#fff"/>
      <line x1="30" y1="13.5" x2="275" y2="13.5" stroke="#777" stroke-width="3"/>
      <line x1="30" y1="13.5" x2="60" y2="13.5" stroke="#fff" stroke-width="3"/>
      <text x="288" y="17" fill="#fff" font-size="10" font-family="Open Sans, sans-serif">0:15</text>
      <path d="M322 10 h4 l5 -4 v15 l-5 -4 h-4 z" fill="#fff"/>
      <line x1="345" y1="13.5" x2="410" y2="13.5" stroke="#fff" stroke-width="3"/>
      <rect x="428" y="8" width="14" height="11" fill="none" stroke="#fff" stroke-width="2"/>
    </svg>
  </div>
</div>

<section class="abs strip">
  <span style="left:328px">“Top</span>
  <span style="left:478px">Most Promising Data Analytics Company”</span>
</section>
<div class="abs badge">20</div>

<div class="abs about-art" role="img" aria-label="Illustration of a phone surrounded by analytics icons on an orbit"></div>
<article class="abs about">
  <h2>About Us</h2>
  <p>Are your apps inspiring and insightful? We are a boutique company focused on mobile and predictive analytics products and solutions. Our software products, such as Brightwell Decisions, leverage predictive analytics, and a compelling user experience, to assist our clients in achieving game changing benefits in their marketplace.</p>
  <div class="btn-small">Learn More
    <svg width="10" height="12" viewBox="0 0 10 12"><path d="M1 1 L9 6 L1 11 Z" fill="none" stroke="#1a9fd0" stroke-width="1.5"/></svg>
  </div>
</article>

<section class="abs banner" role="img" aria-label="Illustrated sea with sailboat and clouds"></section>
<div class="abs banner-ribbon">Wins Wholesale Industry Solutions App Challenge</div>

<div class="abs service" style="left:95px">
  <div class="service-disc">
    <svg width="80" height="60" viewBox="0 0 80 60" fill="none" stroke="#fff" stroke-width="5" stroke-linejoin="round">
      <rect x="4" y="6" width="44" height="36" rx="4"/><path d="M48 18 h16 l12 14 v10 h-28z"/>
      <circle cx="18" cy="48" r="7" fill="#7ccdf7"/><circle cx="60" cy="48" r="7" fill="#7ccdf7"/>
    </svg>
  </div>
  <h3>Wholesale Distribution</h3>
  <div class="btn-small">Dicover</div>
</div>
<div class="abs service" style="left:356px">
  <div class="service-disc">
    <svg width="70" height="60" viewBox="0 0 70 60" fill="none" stroke="#fff" stroke-width="5" stroke-linejoin="round">
      <rect x="4" y="14" width="62" height="42" rx="6"/><path d="M24 14 v-8 h22 v8"/><line x1="18" y1="30" x2="52" y2="30"/><line x1="18" y1="42" x2="52" y2="42"/>
    </svg>
  </div>
  <h3>Solution Selling</h3>
  <div class="btn-small">Dicover</div>
</div>
<div class="abs service" style="left:608px">
  <div class="service-disc">
    <svg width="70" height="70" viewBox="0 0 70 70" fill="none" stroke="#fff" stroke-width="5" stroke-linejoin="round">
      <path d="M30 5 h10 l2 9 l7 3 l8 -5 l7 7 l-5 8 l3 7 l9 2 v10 l-9 2 l-3 7 l5 8 l-7 7 l-8 -5 l-7 3 l-2 9 h-10 l-2 -9 l-7 -3 l-8 5 l-7 -7 l5 -8 l-3 -7 l-9 -2 v-10 l9 -2 l3 -7 l-5 -8 l7 -7 l8 5 l7 -3 z"/>
      <circle cx="35" cy="35" r="10"/>
    </svg>
  </div>
  <h3>Capacity Planning</h3>
  <div class="btn-small">Dicover</div>
</div>
<div class="abs service" style="left:859px">
  <div class="service-disc">
    <svg width="64" height="64" viewBox="0 0 64 64" fill="none" stroke="#fff" stroke-width="6" stroke-linecap="round">
      <circle cx="10" cy="54" r="4" fill="#fff"/><path d="M8 34 a22 22 0 0 1 22 22"/><path d="M8 20 a36 36 0 0 1 36 36"/><path d="M8 6 a50 50 0 0 1 50 50"/>
    </svg>
  </div>
  <h3>Mobile Solutions</h3>
  <div class="btn-small">Dicover</div>
</div>

<section class="abs forum">Showcased at Nordline Core Startup Forum</section>
<div class="abs partners-cap">
  <h2>Featured Partners</h2>
  <svg width="12" height="10" viewBox="0 0 12 10"><path d="M0 0 H12 L6 10 Z" fill="#1a9fd0"/></svg>
</div>
<div class="abs arrow-btn" style="left:120px">
  <svg width="40" height="40" viewBox="0 0 40 40"><path d="M23 12 L15 20 L23 28" fill="none" stroke="#aaa" stroke-width="2.5"/></svg>
</div>
<span class="abs partner" style="left:262px">Cloudmere</span>
<span class="abs partner" style="left:540px;font-weight:600;letter-spacing:1px">Vantrix</span>
<span class="abs partner" style="left:790px;font-weight:700">Nordline</span>
<div class="abs arrow-btn" style="left:1035px">
  <svg width="40" height="40" viewBox="0 0 40 40"><path d="M17 12 L25 20 L17 28" fill="none" stroke="#aaa" stroke-width="2.5"/></svg>
</div>

<section class="abs blog"></section>
<h2 class="abs blog-title">Post Blogs</h2>
<svg class="abs" style="left:605px;top:2250px" width="12" height="10" viewBox="0 0 12 10"><path d="M0 0 H12 L6 10 Z" fill="#2a3843"/></svg>
<div class="abs timeline"></div>

<div class="abs post-photo" style="left:523px;top:2353px"><div role="img" aria-label="Author portrait photo"></div></div>
<article class="abs post" style="left:718px;top:2370px;width:345px">
  <h3>QOS 8 – What do you need to know?</h3>
  <p>Its Finally Here! Its easy to overlook the challenges in upgrading an existing install base to a new version...</p>
  <time>SEPTEMBER 17, 2014</time>
  <div class="more">Read More
    <svg width="22" height="22" viewBox="0 0 22 22"><circle cx="11" cy="11" r="9.5" fill="none" stroke="#222" stroke-width="1.5"/><path d="M9 6.5 L13.5 11 L9 15.5" fill="none" stroke="#222" stroke-width="1.8"/></svg>
  </div>
</article>

<div class="abs post-photo" style="left:523px;top:2577px"><div role="img" aria-label="Author portrait photo"></div></div>
<article class="abs post" style="left:122px;top:2608px;width:370px;text-align:right">
  <h3>Partner Portal Launch!</h3>
  <p>Brightwell Analytics is pleased to announce the launch of our partner portal. This portal is being updated frequently with best...</p>
  <time>SEPTEMBER 17, 2014</time>
  <div class="more">Read More
    <svg width="22" height="22" viewBox="0 0 22 22"><circle cx="11" cy="11" r="9.5" fill="none" stroke="#222" stroke-width="1.5"/><path d="M9 6.5 L13.5 11 L9 15.5" fill="none" stroke="#222" stroke-width="1.8"/></svg>
  </div>
</article>

<footer class="abs footer">
  <span class="abs" style="left:144px;top:21px">©2014 Brightwell Analytics</span>
  <span class="abs social" style="left:949px"></span>
  <span class="abs social" style="left:988px"></span>
  <span class="abs social" style="left:1027px"></span>
</footer>

</body>
</html>
```